VANTAGE FLEET Infographic

We are looking for an infographic style design for Kelvor Freight's VANTAGE FLEET Program. This is a program for truck drivers to help encourage fuel efficiency. The "VANTAGE" is also an acronym and each letter represents a tip of improving fuel efficiency. This (the acronym and the tips) is what will make up the content for the infographic. These are listed below and in the attached .pdf for your reference.

NOTE: The PDF is just for reference. This project is not meant to recreate the PDF, but rather take the info from the PDF and translate that into an infographic.

Minimize RPM’s
• Use Cruise Control in Top Gear whenever possible. The difference between 54 PMG in 9th gear vs. 10th gear is 1.0 MPG, and using Cruise will minimize RPM fluctuations.
• Let it roll! Disable the Torvin Retarder when coasting to a stop. The Torvin Retarder is an important safety feature to assist with speed reduction in emergencies, but increases RPM’s…decreasing MPG’s

Idle Off – reduce idle whenever possible. For every house of idle, we use 1 gallon of fuel. That’s $4/hour to idle your truck.!

Speed – Reduce your speed whenever practical. For every mile per hour reduction in speed while in top gear, an additional 0.1MPG can be achieved.

Shifting Techniques – Progressive Shift is the quickest and most economical way to get your truck up to cruising speed. It minimizes RPM fluctuation and keeps the engine near peak torque and peak horsepower.

Inflation and Inspection
• Check your tire pressures daily. Maintaining steers at 110 lbs. and drive tires at 100lbs will significantly reduce rolling resistance. Every 10 PSI below this results in 0.05 MPG loss.
• Check your fluid levels daily and top them off as needed for peak truck efficiency.

On Time Maintenance – Make sure you get your preventive maintenance services done on time. Proper on time maintenance will ensure your truck is running at peak efficiency.

Narrow the Gap – by minimizing the gap between the tractor and trailer, you can improve aerodynamics. Having a gap in excess of 30 inches can increase drag by over 2%.

So, this content will make up the infographic and each of the first letters in the tips spells "VANTAGE" so those letters should be nice and large to stand out.

The call to action (CTA) on the infographic is to visit GoVantageFleet.example

I have attached the VANTAGE FLEET logo and the Kelvor Freight logo to be used in the branding of the infographic as well.

Target Market(s)

Potential truck drivers - ages (roughly) 25 - 55

Industry/Entity Type

Safety

Requirements
Must have
• This must be infographic style - this is not a project to recreate the attached PDF...this is an infographic that takes the information, interprets it and represents it with graphics.
Should not have
• This is not a document creation project, but an infographic that represents the information with graphics to illustrate each point.

```html
<!DOCTYPE html>
<html lang="en">
<head>
<meta charset="utf-8">
<title>VANTAGE FLEET – Kelvor Freight</title>
<link href="https://fonts.googleapis.com/css2?family=Oswald:wght@600;700&family=Open+Sans:ital,wght@0,400;0,600;1,600;1,700&display=swap" rel="stylesheet">
<style>
  :root{
    --bg-top:#f7fafa;
    --bg-bottom:#d9efe9;
    --ink:#1c1c1c;
    --title-red:#8e1a1d;
    --title-gray:#5d6166;
    --brand-red:#c8202a;
    --purple:#9b92f2;
    --teal-green:#22c08c;
    --green:#2db884;
    --lime:#8cc63f;
    --leaf:#79c043;
    --blue:#2ba3d9;
    --aqua:#2bb1c9;
    --orange:#f7a833;
    --slate:#4d5866;
    --cta-dark:#3c3f43;
    --cta-red:#a8151b;
  }
  *{box-sizing:border-box;margin:0;padding:0}
  html,body{width:720px;height:1200px;overflow:hidden}
  body{font-family:"Open Sans",Arial,sans-serif;color:var(--ink)}
  .canvas{position:relative;width:720px;height:1200px;overflow:hidden;
    background:linear-gradient(180deg,var(--bg-top) 0%,#eef7f5 45%,var(--bg-bottom) 100%)}
  .connectors{position:absolute;inset:0}
  .program-mark{position:absolute;left:18px;top:26px;display:flex;align-items:center;gap:8px;
    font-family:"Oswald",sans-serif;font-weight:700;font-size:22px;color:var(--title-red);line-height:1}
  .program-mark .dot{width:22px;height:22px;border-radius:50%;background:var(--title-red)}
  .company-mark{position:absolute;right:22px;top:36px;font-family:"Oswald",sans-serif;
    font-weight:700;font-size:34px;color:var(--brand-red);line-height:1}
  .title{position:absolute;left:0;right:16px;top:118px;text-align:right;
    font-family:"Oswald",sans-serif;font-weight:700;font-size:80px;line-height:1;letter-spacing:1px}
  .title .word-a{color:var(--title-red)}
  .title .word-b{color:var(--title-gray)}
  .letter{position:absolute;display:flex;align-items:center;justify-content:center;
    font-family:"Open Sans",sans-serif;font-size:48px;line-height:1;color:var(--ink)}
  .panel{position:absolute;padding:6px 7px;font-size:10.5px;line-height:1.3}
  .panel h2{font-weight:400;font-size:19px;line-height:1.1;margin-bottom:3px}
  .panel h2 .cap{font-size:30px}
  .panel ul{list-style:none}
  .panel li::before{content:"• "}
  .truck{position:absolute;left:267px;top:349px;width:400px;height:140px;
    background:linear-gradient(180deg,#5a6572,var(--slate));border-radius:6px 30px 6px 6px}
  .art{border-radius:4px}
  .cta{position:absolute;left:133px;top:1049px;width:467px;height:124px;border-radius:60px;overflow:hidden;
    box-shadow:0 4px 10px rgba(0,0,0,.35)}
  .cta .top{height:58px;background:linear-gradient(180deg,#5b5f64,var(--cta-dark));color:#fff;
    display:flex;align-items:center;justify-content:center;font-size:33px;font-style:italic;font-weight:600}
  .cta .top b{font-weight:700;margin-left:8px}
  .cta .bottom{height:66px;background:linear-gradient(180deg,#c21d24,var(--cta-red));color:#fff;
    display:flex;align-items:center;justify-content:center;font-size:27px;font-weight:600}
</style>
</head>
<body>
<div class="canvas">
  <svg class="connectors" width="720" height="1200" viewBox="0 0 720 1200" fill="none" stroke-width="5">
    <polyline points="96,298 157,298" stroke="var(--purple)"/>
    <polyline points="513,298 680,298 680,453" stroke="var(--purple)"/>
    <circle cx="680" cy="453" r="7" fill="var(--purple)"/>
    <polyline points="115,440 115,460" stroke="var(--teal-green)"/>
    <polyline points="147,405 330,405 330,440" stroke="var(--teal-green)"/>
    <polyline points="205,540 205,693" stroke="var(--lime)"/>
    <polyline points="237,505 300,505 300,470" stroke="var(--lime)"/>
    <polyline points="307,613 307,640 215,640 215,867" stroke="var(--leaf)"/>
    <polyline points="307,547 307,505 360,505 360,430" stroke="var(--leaf)"/>
    <circle cx="360" cy="430" r="7" fill="var(--leaf)"/>
    <polyline points="290,497 640,497" stroke="var(--blue)"/>
    <polyline points="430,587 430,497" stroke="var(--blue)"/>
    <polyline points="400,653 400,753" stroke="var(--blue)"/>
    <polyline points="562,593 562,497" stroke="var(--aqua)"/>
    <polyline points="540,656 540,780" stroke="var(--aqua)"/>
    <polyline points="680,560 680,525 587,525 587,452" stroke="var(--orange)"/>
    <circle cx="587" cy="452" r="7" fill="var(--orange)"/>
    <polyline points="680,627 680,720" stroke="var(--orange)"/>
    <g fill="var(--blue)">
      <circle cx="310" cy="512" r="5"/><circle cx="360" cy="512" r="5"/>
      <circle cx="420" cy="512" r="5"/><circle cx="520" cy="512" r="5"/><circle cx="620" cy="512" r="5"/>
    </g>
  </svg>

  <div class="program-mark"><span class="dot"></span>VANTAGE FLEET</div>
  <div class="company-mark">Kelvor Freight</div>

  <h1 class="title"><span class="word-a">VANTAGE</span> <span class="word-b">FLEET</span></h1>

  <div class="truck" role="img" aria-label="Silhouette of a tractor-trailer truck"></div>

  <div class="letter" style="left:24px;top:263px;width:72px;height:70px;background:var(--purple)">M</div>
  <section class="panel" style="left:157px;top:237px;width:356px;height:140px;background:var(--purple)">
    <h2><span class="cap">M</span>inimize RPM’s</h2>
    <ul>
      <li>Use Cruise Control in Top Gear whenever possible. The difference between 54 MPH in 9th gear vs. 10th gear is 1.0 MPG, and using Cruise will minimize RPM fluctuations.</li>
      <li>Let it roll! Disable the Torvin Retarder when coasting to a stop. The Torvin Retarder is an important safety feature to assist with speed reduction in emergencies, but increases RPM’s…decreasing MPG’s.</li>
    </ul>
  </section>

  <div class="letter" style="left:83px;top:373px;width:64px;height:67px;background:var(--teal-green)">I</div>
  <section class="panel" style="left:7px;top:460px;width:186px;height:220px;background:var(--green)">
    <h2><span class="cap">I</span>dle Off</h2>
    <p>Reduce idle whenever possible. For every hour of idle, we use 1 gallon of fuel. That’s $4/hour to idle your truck!</p>
    <div class="art" role="img" aria-label="Idling truck with exhaust smoke" style="margin-top:8px;height:100px;background:linear-gradient(180deg,#7d8a8f,#4d5866)"></div>
  </section>

  <div class="letter" style="left:173px;top:473px;width:64px;height:67px;background:var(--lime)">S</div>
  <section class="panel" style="left:7px;top:693px;width:193px;height:154px;background:var(--lime)">
    <h2><span class="cap">S</span>peed</h2>
    <p>Reduce your speed whenever practical. For every mile per hour reduction in speed while in top gear, an additional 0.1 MPG can be achieved.</p>
    <div class="art" role="img" aria-label="Speedometer gauge" style="margin:6px auto 0;width:70px;height:40px;border-radius:40px 40px 4px 4px;background:#3f4a45"></div>
  </section>

  <div class="letter" style="left:273px;top:547px;width:67px;height:66px;background:var(--leaf)">S</div>
  <section class="panel" style="left:7px;top:867px;width:217px;height:162px;background:var(--leaf)">
    <h2><span class="cap">S</span>hifting Techniques</h2>
    <p>Progressive Shift is the quickest and most economical way to get your truck up to cruising speed. It minimizes RPM fluctuation and keeps the engine near peak torque and peak horsepower.</p>
    <svg width="60" height="36" viewBox="0 0 60 36" style="margin:4px 0 0 20px" font-size="9" fill="#1c1c1c" stroke="#1c1c1c" stroke-width="1.5">
      <line x1="8" y1="9" x2="8" y2="27"/><line x1="24" y1="9" x2="24" y2="27"/><line x1="40" y1="9" x2="40" y2="27"/>
      <line x1="8" y1="18" x2="40" y2="18"/>
      <g stroke="none"><text x="5" y="8">1</text><text x="21" y="8">3</text><text x="37" y="8">5</text>
      <text x="5" y="35">2</text><text x="21" y="35">4</text><text x="37" y="35">R</text></g>
    </svg>
  </section>

  <div class="letter" style="left:400px;top:587px;width:60px;height:66px;background:var(--blue)">I</div>
  <section class="panel" style="left:260px;top:753px;width:167px;height:270px;background:var(--blue);font-size:10px">
    <h2><span class="cap">I</span>nflation and Inspection</h2>
    <ul>
      <li>Check your tire pressures daily. Maintaining steers at 110 lbs. and drive tires at 100 lbs. will significantly reduce rolling resistance. Every 10 PSI below this results in 0.05 MPG loss.</li>
      <li>Check your fluid levels daily and top them off as needed for peak truck efficiency.</li>
    </ul>
    <div class="art" role="img" aria-label="Truck tire" style="margin:6px auto 0;width:50px;height:50px;border-radius:50%;background:#1f2a33"></div>
  </section>

  <div class="letter" style="left:531px;top:593px;width:62px;height:63px;background:var(--aqua)">O</div>
  <section class="panel" style="left:437px;top:780px;width:130px;height:243px;background:var(--aqua)">
    <h2><span class="cap">O</span>n Time Maintenance</h2>
    <p>Make sure you get your preventive maintenance services done on time. Proper on time maintenance will ensure your truck is running at peak efficiency.</p>
    <div class="art" role="img" aria-label="Clock with wrench and screwdriver" style="margin-top:8px;height:52px;background:#263238"></div>
  </section>

  <div class="letter" style="left:647px;top:560px;width:66px;height:67px;background:var(--orange)">N</div>
  <section class="panel" style="left:576px;top:720px;width:137px;height:303px;background:var(--orange)">
    <h2><span class="cap">N</span>arrow the Gap</h2>
    <p>By minimizing the gap between the tractor and trailer, you can improve aerodynamics. Having a gap in excess of 30 inches can increase drag by over 2%.</p>
    <div class="art" role="img" aria-label="Truck with wide tractor-trailer gap" style="margin-top:10px;height:36px;background:#4d5866"></div>
    <div class="art" role="img" aria-label="Truck with narrow tractor-trailer gap" style="margin-top:14px;height:36px;background:#4d5866"></div>
  </section>

  <div class="cta">
    <div class="top">Save Fuel. <b>Click Here.</b></div>
    <div class="bottom">GoVantageFleet.example</div>
  </div>
</div>
</body>
</html>
```